Design for Perch Lane real estate agency

Incorporate logo into new business cards. I need to include the Marlowe Ridge logo incorporated into Perch Lane on one side of the card (attached). On the other side I see just the icon with "Tessa Lorne" (attached) with "Rooted in Care" either included as is or removed from logo and rather put as a tag line on the business card separate from the main logo. Contact information:

Tessa Lorne
Associate Broker
Cell: 914-555-0173
Email: tessalorne@perchlane.example
Web: www.perchlane.example

Target Market(s)

Buyers, Sellers, Builders and Investors of homes and land

Industry/Entity Type

Real Estate Agent

Contact Information for Business Card

My client base tend to be higher end home buyers, sellers, builders and investors. I have been more and more in land and subdivisions for builders and investors. The card should not be cluttered. Clean and simple - yet with an air of exclusive/high end

Colors

Designer to choose colors to be used in the design.

Requirements
Must have
• Must have the logo on one side that has Marlowe Ridge logo incorporated. The side that has my contact information does not have to have the Marlowe Ridge logo incorporated.
• Must include "Rooted in Care" tag line either within logo (as is) or removed from logo and included in another position on the side of the business card with contact information.
Should not have
• Should not have Marlowe Ridge logo incorporated into Perch Lane logo on both sides of business card. Would like the Perch Lane logo that has Marlowe Logo only on the back side of card without contact information.

```html
<!DOCTYPE html>
<html lang="en">
<head>
<meta charset="utf-8">
<title>Perch Lane – Business Cards</title>
<link rel="stylesheet" href="https://fonts.googleapis.com/css2?family=Montserrat:wght@400;500;600&display=swap">
<style>
  :root {
    --backdrop: #3a3a3a;
    --card: #ffffff;
    --brown: #5c3d14;
    --brown-text: #3d2a12;
    --gold: #c9a227;
    --grey-text: #4a4a4a;
  }
  * { box-sizing: border-box; margin: 0; padding: 0; }
  html, body { width: 1200px; height: 864px; overflow: hidden; }
  body {
    background: var(--backdrop);
    font-family: "Montserrat", sans-serif;
    position: relative;
  }
  .card {
    position: absolute;
    width: 560px;
    height: 320px;
    background: var(--card);
    box-shadow: 0 10px 30px rgba(0,0,0,.45);
    overflow: hidden;
  }
  .card--front { left: 320px; top: 80px; }
  .card--back  { left: 320px; top: 464px; }

  /* Front: brand lockup */
  .lockup {
    position: absolute;
    left: 0; right: 0; top: 108px;
    display: flex; align-items: center; justify-content: center; gap: 14px;
  }
  .lockup__mark {
    width: 30px; height: 30px; border-radius: 50%;
    background: var(--gold);
  }
  .lockup__text { display: flex; flex-direction: column; }
  .lockup__name {
    font-size: 30px; font-weight: 500; color: var(--brown); line-height: 1;
  }
  .lockup__agent {
    margin-top: 6px;
    font-size: 10px; letter-spacing: 3px; text-transform: uppercase;
    color: var(--brown-text); border-top: 1px solid var(--gold); padding-top: 4px;
  }
  .lockup__tag {
    font-size: 6px; letter-spacing: 2.5px; text-transform: uppercase;
    color: var(--brown-text); margin-top: 2px;
  }
  .partner-badge {
    width: 44px; height: 22px; background: var(--brown);
    align-self: flex-start; margin-top: 4px;
  }
  .front__web {
    position: absolute; left: 0; right: 0; bottom: 52px;
    text-align: center; font-size: 14px; color: var(--brown-text);
  }

  /* Back: contact side */
  .agent-mark {
    position: absolute; right: 34px; top: 34px;
    display: flex; align-items: center; gap: 10px;
  }
  .agent-mark__dot { width: 26px; height: 26px; border-radius: 50%; background: var(--gold); }
  .agent-mark__name {
    font-size: 18px; font-weight: 500; letter-spacing: 3px;
    text-transform: uppercase; color: var(--brown);
  }
  .agent-mark__tag {
    font-size: 6px; letter-spacing: 2.5px; text-transform: uppercase;
    color: var(--brown-text); margin-top: 2px;
  }
  .contact { position: absolute; left: 40px; top: 170px; }
  .contact__name { font-size: 20px; font-weight: 600; color: var(--brown-text); }
  .contact__role { font-size: 13px; color: var(--gold); margin-top: 2px; }
  .contact__list { list-style: none; margin-top: 18px; }
  .contact__item {
    display: flex; align-items: center; gap: 10px;
    font-size: 13px; color: var(--grey-text); line-height: 22px;
  }
  .contact__item svg { width: 12px; height: 12px; fill: var(--gold); flex: none; }
  .wave { position: absolute; left: 0; bottom: 0; width: 560px; height: 320px; }
  .wave__tagline {
    position: absolute; right: 26px; bottom: 22px;
    font-size: 13px; color: #fff;
  }
</style>
</head>
<body>

<section class="card card--front" aria-label="Card front">
  <div class="lockup">
    <span class="lockup__mark"></span>
    <div class="lockup__text">
      <span class="lockup__name">Perch Lane</span>
      <span class="lockup__agent">Tessa Lorne</span>
      <span class="lockup__tag">Rooted in Care</span>
    </div>
    <span class="partner-badge" aria-label="Marlowe Ridge partner badge"></span>
  </div>
  <p class="front__web">www.perchlane.example</p>
</section>

<section class="card card--back" aria-label="Card back">
  <div class="agent-mark">
    <span class="agent-mark__dot"></span>
    <div>
      <div class="agent-mark__name">Tessa Lorne</div>
      <div class="agent-mark__tag">Rooted in Care</div>
    </div>
  </div>

  <svg class="wave" viewBox="0 0 560 320" aria-hidden="true">
    <path d="M150,320 Q380,250 560,228 L560,246 Q380,262 200,320 Z" fill="var(--gold)"/>
    <path d="M250,320 Q420,262 560,252 L560,320 Z" fill="var(--brown)"/>
  </svg>
  <span class="wave__tagline">rooted in care</span>

  <div class="contact">
    <h1 class="contact__name">Tessa Lorne</h1>
    <p class="contact__role">Associate Broker</p>
    <ul class="contact__list">
      <li class="contact__item">
        <svg viewBox="0 0 12 12"><path d="M3 0h6a1 1 0 0 1 1 1v10a1 1 0 0 1-1 1H3a1 1 0 0 1-1-1V1a1 1 0 0 1 1-1zm0 1.5v8h6v-8z"/></svg>
        914-555-0173
      </li>
      <li class="contact__item">
        <svg viewBox="0 0 12 12"><path d="M0 2h12v8H0zM1 3l5 3.5L11 3v-.2H1z"/></svg>
        tessalorne@perchlane.example
      </li>
      <li class="contact__item">
        <svg viewBox="0 0 12 12"><path d="M6 0a6 6 0 1 0 0 12A6 6 0 0 0 6 0zm0 1c.8 0 1.6 1.8 1.8 4H4.2C4.4 2.8 5.2 1 6 1zM1.1 5h2.1c.1-1.4.4-2.6.9-3.5A5 5 0 0 0 1.1 5zm0 2a5 5 0 0 0 3 3.5C3.6 9.6 3.3 8.4 3.2 7zm3.1 0h3.6C7.6 9.2 6.8 11 6 11S4.4 9.2 4.2 7zm4.6 0h2.1a5 5 0 0 1-3 3.5c.5-.9.8-2.1.9-3.5zm2.1-2H8.8c-.1-1.4-.4-2.6-.9-3.5a5 5 0 0 1 3 3.5z"/></svg>
        www.perchlane.example
      </li>
    </ul>
  </div>
</section>

</body>
</html>
```